PawQuarry Banner contest an ecommerce site for veterinarians

We need banners for our ecommerce site. Our site is a webstore that veterinarians can use to allow their clients to purchase items from them. Each month we have a different theme for our banners. I am looking for banners for January and February and with a refresh coming to our site could be looking at a dozen over the next year. I may potentially choose from multiple designers and increase the payment or will choose one designer for both months .

For January our theme is winter fun. We will be running a contest were people can submit a picture of their pet to our Chatterloop page enjoying the snow or keeping warm. they have a chance to win one of 5 $50 gift certificates to pawquarry. The banner should have a dog and cat and a separate one with just a cat. We will need a French and English banner. We will provide the French translation once the winner has been selected.

For February our theme is dental health. The banner should have a dog and cat and a separate one with just a cat. We will need a French and English banner. We will provide the French translation once the winner has been selected.

Target Market(s)

pet owners

Industry/Entity Type

Veterinary

Colors

Designer to choose colors to be used in the design.

Requirements
Must have
• dimensions for PQ Banner are: 710px x 280px
Nice to have
• I have attached our logo and some screen shoots of our site so you can get a feel of what it look like. you could also go to www.pawquarry.ca and see what the sign in page looks like
Should not have
• images of pet food

```html
<!DOCTYPE html>
<html lang="en">
<head>
<meta charset="utf-8">
<title>Pet Dental Health Month Banner</title>
<link rel="stylesheet" href="https://fonts.googleapis.com/css2?family=Roboto+Condensed:wght@300;400&family=Open+Sans:wght@400;600&display=swap">
<style>
  :root {
    --bg: #ffffff;
    --smile-blue: #7fa6e0;
    --heading-grey: #8a8a8a;
    --panel-blue: #6b93dd;
    --panel-blue-soft: rgba(107, 147, 221, 0);
    --band-blue: #4f78c8;
    --band-blue-light: #7fa1e0;
    --panel-text: #ffffff;
    --cat-light: #f3e6d9;
    --cat-mid: #e6c7a8;
    --cat-warm: #d8a57c;
    --tooth-white: #fbfdff;
    --tooth-edge: #9db8e6;
    --brush-pink: #f3b4c4;
    --paste-blue: #3f6bc1;
  }
  html, body {
    margin: 0;
    padding: 0;
    overflow: hidden;
    background: var(--bg);
  }
  .banner {
    position: relative;
    width: 1200px;
    height: 473px;
    overflow: hidden;
    background: var(--bg);
    font-family: "Open Sans", Arial, sans-serif;
  }
  .cat-photo {
    position: absolute;
    left: 760px;
    top: 0;
    width: 440px;
    height: 473px;
    background:
      radial-gradient(ellipse 60% 55% at 55% 45%, var(--cat-warm) 0%, var(--cat-mid) 45%, rgba(243,230,217,0) 80%),
      linear-gradient(90deg, rgba(255,255,255,1) 0%, var(--cat-light) 35%, var(--cat-light) 100%);
  }
  .headline {
    position: absolute;
    left: 0;
    top: 40px;
    width: 700px;
    text-align: right;
    font-family: "Roboto Condensed", "Arial Narrow", sans-serif;
    font-weight: 300;
  }
  .headline__smile {
    display: block;
    color: var(--smile-blue);
    font-size: 66px;
    line-height: 1;
    letter-spacing: 1px;
    margin-right: 8px;
  }
  .headline__theme {
    display: block;
    margin-top: 6px;
    color: var(--heading-grey);
    font-size: 48px;
    line-height: 1.1;
    white-space: nowrap;
  }
  .headline__lead {
    font-size: 30px;
    font-weight: 400;
  }
  .care-panel {
    position: absolute;
    left: 93px;
    top: 203px;
    width: 583px;
    height: 240px;
    color: var(--panel-text);
  }
  .care-panel__top {
    height: 147px;
    padding: 14px 24px 0;
    box-sizing: border-box;
    background: linear-gradient(90deg, var(--panel-blue) 0%, #8fb0ea 65%, #c9daf6 100%);
  }
  .care-panel__title {
    margin: 0;
    font-family: "Roboto Condensed", "Arial Narrow", sans-serif;
    font-weight: 300;
    font-size: 42px;
    line-height: 1.15;
  }
  .care-panel__body {
    margin: 8px 0 0;
    font-size: 22px;
    line-height: 1.3;
    max-width: 520px;
  }
  .care-panel__band {
    height: 93px;
    padding: 12px 24px 0;
    box-sizing: border-box;
    background: linear-gradient(90deg, var(--band-blue) 0%, var(--band-blue-light) 100%);
    font-size: 21px;
    line-height: 1.4;
    font-weight: 600;
  }
  .tooth-mascot {
    position: absolute;
    left: 540px;
    top: 308px;
    width: 100px;
    height: 100px;
  }
  .brush-and-paste {
    position: absolute;
    left: 556px;
    top: 392px;
    width: 444px;
    height: 64px;
  }
</style>
</head>
<body>
<div class="banner">
  <div class="cat-photo" role="img" aria-label="Photo of a cream-coloured cat leaning down to sniff a toothbrush"></div>

  <div class="headline">
    <span class="headline__smile">SMILE !</span>
    <span class="headline__theme"><span class="headline__lead">It's </span>Pet Dental Health Month</span>
  </div>

  <section class="care-panel">
    <div class="care-panel__top">
      <h2 class="care-panel__title">Dental Care</h2>
      <p class="care-panel__body">Bad breath is not a normal nuisance - it's sign of dental disease.</p>
    </div>
    <div class="care-panel__band">Keep your pet healthy and happy<br>by maintining their dental health!</div>
  </section>

  <svg class="tooth-mascot" viewBox="0 0 100 100" role="img" aria-label="Illustration of a smiling cartoon tooth mascot">
    <circle cx="50" cy="50" r="46" fill="var(--tooth-white)" stroke="var(--tooth-edge)" stroke-width="3"/>
  </svg>

  <svg class="brush-and-paste" viewBox="0 0 444 64" role="img" aria-label="Photo of a tube of toothpaste and a pink toothbrush">
    <defs>
      <linearGradient id="brushToneFill" x1="0" x2="1" y1="0" y2="0">
        <stop offset="0" stop-color="var(--paste-blue)"/>
        <stop offset="0.35" stop-color="#e7ecf5"/>
        <stop offset="0.55" stop-color="var(--brush-pink)"/>
        <stop offset="1" stop-color="#f7dbe3"/>
      </linearGradient>
    </defs>
    <rect x="0" y="14" width="444" height="36" rx="18" fill="url(#brushToneFill)" opacity="0.8"/>
  </svg>
</div>
</body>
</html>
```